Personalized Technology Company Needs a Business Card

I need a double-sided business card. Both sides will have the logo, and the contact information. One side will be black, with the white / gray logo, and the other will be white, with the black / gray logo. The black side will have the text "Custom Gaming PC's" and will have a water-cooled gaming PC image. The white side will have the text "Custom Business Computers & Consulting", and will have a business / enterprise PC image. Feel free to add a conservative image in the background, while the color remains unchanged. I'm uploading the base logo (transparent), so you can modify the colors, both the finished colored logos and an idea of ​​the business card (with the current information, just missing the website, which is www.volinexsystems.com, please add it.) Thank you so much for your effort, I'll be specting your cool designs. Good Luck!

Target Market(s)

Gamers & Entrepreneurs / Business Owners / Chief Technology Officers

Industry/Entity Type

Technology Equipment

Contact Information for Business Card

I need a double-sided business card. Both sides will have the logo, and the contact information. One side will be black, with the white/gray logo, and the other one will be white, with the black/gray logo. The black side will have the text "Custom Gaming PC's" and will have a water-cooled gaming PC image. The white side will have the text "Custom Business Computers & Consulting", and will have a business/enterprise PC image. Feel free to add a conservative image in the background, whilst the color remains unchanged.

I'm uploading the base logo (transparent), so you can modify the colors, both the finished colored logos and an idea of the business card (with the actual information, just missing the website, which is www.volinexsystems.com, please add it.)

Thank you so much for your effort, I'll be specting your cool designs. Good Luck!

Font styles to use
Serif

Colors
000000
757575
ffffff

Requirements
Must have
• Please See Description
Nice to have
• Please See Description
Should not have
• Please See Description

```html
<!DOCTYPE html>
<html lang="en">
<head>
<meta charset="utf-8">
<title>Volinex Systems – Business Cards</title>
<link rel="stylesheet" href="https://fonts.googleapis.com/css2?family=Archivo:wght@800&family=Arimo:wght@400&family=Roboto+Condensed:wght@300&display=swap">
<style>
  :root {
    --black: #000000;
    --ink: #1e1e1e;
    --grey: #757575;
    --white: #ffffff;
    --cream: #ece6df;
    --backdrop: #e4e4e6;
  }
  html, body { margin: 0; padding: 0; overflow: hidden; }
  body {
    width: 1200px; height: 1200px;
    background: var(--backdrop);
    position: relative;
    font-family: "Arimo", Arial, sans-serif;
  }
  .card {
    position: absolute; left: 199px;
    width: 839px; height: 482px;
    overflow: hidden;
  }
  .card--business { top: 78px; background: var(--white); }
  .card--gaming { top: 639px; background: var(--black); }
  .card__art { position: absolute; inset: 0; }

  .tagline { position: absolute; left: 32px; color: var(--cream); font-family: "Archivo", Arial, sans-serif; font-weight: 800; line-height: 1; }
  .tagline__kicker { display: block; font-size: 30px; letter-spacing: 13px; }
  .tagline__main { display: block; font-size: 58px; margin-top: 4px; }
  .tagline__sub { display: block; font-size: 31px; margin-top: 6px; }
  .card--business .tagline { top: 262px; }
  .card--gaming .tagline { top: 238px; left: 44px; }

  .brand {
    position: absolute; right: 33px; top: 92px;
    display: flex; align-items: center; gap: 14px;
    font-family: "Arimo", Arial, sans-serif; font-size: 34px; letter-spacing: 5px;
  }
  .brand__mark { width: 20px; height: 20px; border-radius: 50%; background: var(--grey); }
  .card--business .brand { color: var(--black); }
  .card--gaming .brand { color: var(--white); }

  .contact { position: absolute; right: 34px; top: 222px; text-align: right; }
  .contact__name { font-size: 34px; margin: 0; line-height: 1; }
  .contact__role { font-size: 21px; margin: 4px 0 0; }
  .contact__phone { font-size: 25px; margin: 0; line-height: 32px; }
  .contact__phones { margin-top: 30px; }
  .contact__email { font-family: "Roboto Condensed", Arial, sans-serif; font-weight: 300; font-size: 23px; margin: 16px 0 0; }
  .card--business .contact { color: var(--ink); }
  .card--gaming .contact { color: var(--white); }
</style>
</head>
<body>

<section class="card card--business">
  <svg class="card__art" width="839" height="482" viewBox="0 0 839 482">
    <polygon points="0,0 253,0 518,482 0,482" fill="var(--black)"/>
    <polygon points="264,0 270,0 510,420 506,424" fill="var(--black)"/>
    <g role="img" aria-label="Business desktop computer, monitor and laptop">
      <rect x="30" y="86" width="244" height="164" rx="6" fill="url(#pcTone)"/>
    </g>
    <defs>
      <linearGradient id="pcTone" x1="0" y1="0" x2="1" y2="1">
        <stop offset="0" stop-color="#3a3a3c"/>
        <stop offset="0.55" stop-color="#8a8a8c"/>
        <stop offset="1" stop-color="#1a1a1a"/>
      </linearGradient>
    </defs>
  </svg>
  <h2 class="tagline">
    <span class="tagline__kicker">CUSTOM</span>
    <span class="tagline__main">BUSINESS</span>
    <span class="tagline__sub">COMPUTERS</span>
    <span class="tagline__sub">&amp; CONSULTING</span>
  </h2>
  <div class="brand"><span class="brand__mark"></span>VOLINEX SYSTEMS</div>
  <div class="contact">
    <p class="contact__name">MARCO REYES LUNE</p>
    <p class="contact__role">CEO &amp; CO-FOUNDER</p>
    <div class="contact__phones">
      <p class="contact__phone">+52 5812 - 3390</p>
      <p class="contact__phone">+52 55 - 4186 - 7051</p>
    </div>
    <p class="contact__email">contact@volinexsystems.com</p>
  </div>
</section>

<section class="card card--gaming">
  <svg class="card__art" width="839" height="482" viewBox="0 0 839 482">
    <defs>
      <linearGradient id="rigTone" x1="0" y1="0" x2="1" y2="1">
        <stop offset="0" stop-color="#6c5ab8"/>
        <stop offset="0.4" stop-color="#2b2466"/>
        <stop offset="0.75" stop-color="#3d3f9a"/>
        <stop offset="1" stop-color="#0c0a1c"/>
      </linearGradient>
    </defs>
    <g role="img" aria-label="Water-cooled gaming PC interior with glowing fans">
      <polygon points="0,0 253,0 518,482 0,482" fill="url(#rigTone)"/>
    </g>
    <polygon points="253,0 259,0 380,218 375,218" fill="var(--white)"/>
  </svg>
  <h2 class="tagline">
    <span class="tagline__kicker">CUSTOM</span>
    <span class="tagline__main">GAMING</span>
    <span class="tagline__sub">PC'S</span>
  </h2>
  <div class="brand"><span class="brand__mark"></span>VOLINEX SYSTEMS</div>
  <div class="contact">
    <p class="contact__name">MARCO REYES LUNE</p>
    <p class="contact__role">CEO &amp; CO-FOUNDER</p>
    <div class="contact__phones">
      <p class="contact__phone">+52 5812 - 3390</p>
      <p class="contact__phone">+52 55 - 4186 - 7051</p>
    </div>
    <p class="contact__email">contact@volinexsystems.com</p>
  </div>
</section>

</body>
</html>
```